Glimmerbrook Jubilee. A Magical Holiday Festival

We are having a Glimmerbrook Jubilee festival which will future the following: ice skating rink, snow park, Santa meet and greet, carnival rides, top food trucks, millions of christmas lights, giant inflatables.
Railroad train, Santa House
Snow trough the entire event.
Free for children under 48''
Ticket price: presale $6, at the gate $7.
Glimmer pass: $25

Target Market(s)

Everybody

Industry/Entity Type

Festival

Font styles to use
Decorative

Colors

Designer to choose colors to be used in the design.

Requirements
Must have
• Website adress: glimmerbrookjubileelv.example
• Santa
• Snow flakes
• RQO logo and PLEM logo
• GlimmerbrookJubilee logo
Nice to have
• ice skating rink, Santa house, snow park, christmas lights, christmas tree
Should not have
• sad collors

```html
<!DOCTYPE html>
<html lang="en">
<head>
<meta charset="utf-8">
<title>Glimmerbrook Jubilee LV – A Magical Holiday Festival</title>
<link rel="stylesheet" href="https://fonts.googleapis.com/css2?family=Cinzel:wght@400&family=Roboto:wght@400&family=Abril+Fatface&display=swap">
<style>
  :root {
    --night: #07070b;
    --night-blue: #0d1426;
    --ink-light: #ffffff;
    --gold: #f3cf7a;
    --gold-deep: #b8862e;
    --frame: #ffffff;
    --photo-red: #8a2a22;
    --photo-dusk: #2a3346;
    --photo-lights: #5a1f1a;
    --partner-red: #d8322e;
    --snow: rgba(255,255,255,.85);
  }
  * { margin: 0; padding: 0; box-sizing: border-box; }
  html, body { width: 1200px; height: 444px; overflow: hidden; background: var(--night); }
  .banner {
    position: relative;
    width: 1200px;
    height: 444px;
    overflow: hidden;
    color: var(--ink-light);
    font-family: "Roboto", Arial, sans-serif;
  }
  .festival-scene {
    position: absolute; inset: 0;
    background:
      radial-gradient(circle at 570px 170px, rgba(90,120,200,.55) 0, rgba(40,60,120,.35) 110px, rgba(0,0,0,0) 190px),
      radial-gradient(ellipse 260px 200px at 150px 380px, rgba(200,110,40,.55), rgba(0,0,0,0) 70%),
      radial-gradient(ellipse 200px 160px at 470px 420px, rgba(190,80,40,.45), rgba(0,0,0,0) 70%),
      radial-gradient(ellipse 240px 130px at 700px 440px, rgba(120,40,30,.4), rgba(0,0,0,0) 70%),
      linear-gradient(180deg, var(--night) 0%, var(--night-blue) 55%, #1b0f0a 100%);
  }
  .snowfall { position: absolute; inset: 0; pointer-events: none; }
  .headline {
    position: absolute; left: 46px; top: 44px;
    font-family: "Cinzel", Georgia, serif;
    font-weight: 400;
    text-shadow: 0 2px 6px rgba(0,0,0,.8);
  }
  .headline-title { font-size: 47px; line-height: 54px; font-weight: 400; letter-spacing: 1px; }
  .headline-tagline { font-size: 34px; line-height: 46px; font-weight: 400; letter-spacing: 1.5px; }
  .attractions {
    position: absolute; left: 63px; top: 182px;
    list-style: none;
    font-size: 20.5px;
    line-height: 35.5px;
    text-shadow: 0 1px 4px rgba(0,0,0,.9);
  }
  .attractions li { display: flex; align-items: center; gap: 13px; }
  .attractions svg { flex: none; }
  .dates {
    position: absolute; left: 592px; top: 172px;
    font-family: "Abril Fatface", Georgia, serif;
    font-size: 50px;
    line-height: 66px;
    color: var(--gold);
    text-shadow: 2px 3px 0 var(--gold-deep), 0 4px 10px rgba(0,0,0,.9);
  }
  .pricing {
    position: absolute; right: 274px; top: 244px;
    text-align: right;
    font-size: 22px;
    line-height: 32.5px;
    text-shadow: 0 1px 4px rgba(0,0,0,.9);
  }
  .partners {
    position: absolute; left: 768px; top: 376px;
    display: flex; align-items: center; gap: 26px;
  }
  .partner {
    display: flex; align-items: center; gap: 6px;
    font-size: 17px;
  }
  .partner-dot { width: 12px; height: 12px; border-radius: 50%; background: var(--partner-red); }
  .website {
    position: absolute; left: 768px; top: 410px;
    font-size: 15px;
    letter-spacing: .3px;
    text-shadow: 0 1px 4px rgba(0,0,0,.9);
  }
  .snapshot {
    position: absolute;
    border: 6px solid var(--frame);
    border-radius: 4px;
    box-shadow: 0 4px 10px rgba(0,0,0,.7);
  }
  .snapshot-santa-house { left: 806px; top: 8px; width: 186px; height: 122px; transform: rotate(-4deg);
    background: linear-gradient(160deg, #d9d3c8, var(--photo-red) 60%, #3a2a20); }
  .snapshot-santa-visit { left: 990px; top: 6px; width: 204px; height: 134px; transform: rotate(5deg);
    background: linear-gradient(150deg, #3a3020, var(--photo-red) 55%, #e8e0d6); }
  .snapshot-skating { left: 974px; top: 136px; width: 212px; height: 160px; transform: rotate(3deg);
    background: linear-gradient(180deg, #1a2233, var(--photo-dusk) 50%, #6a7488); }
  .snapshot-light-tree { left: 984px; top: 292px; width: 216px; height: 140px; transform: rotate(-6deg);
    background: radial-gradient(ellipse at 55% 40%, #d25a3a, var(--photo-lights) 45%, #120b12 85%); }
</style>
</head>
<body>
<main class="banner">
  <div class="festival-scene" role="img" aria-label="Night-time festival scene with an illuminated Ferris wheel and buildings covered in warm Christmas lights"></div>

  <svg class="snowfall" width="1200" height="444" viewBox="0 0 1200 444" aria-hidden="true">
    <defs>
      <g id="flake" stroke="var(--snow)" stroke-width="1.6" stroke-linecap="round">
        <line x1="0" y1="-7" x2="0" y2="7"/>
        <line x1="-6" y1="-3.5" x2="6" y2="3.5"/>
        <line x1="-6" y1="3.5" x2="6" y2="-3.5"/>
      </g>
    </defs>
    <use href="#flake" x="360" y="40"/>
    <use href="#flake" x="690" y="28"/>
    <use href="#flake" x="780" y="120"/>
    <use href="#flake" x="420" y="160"/>
    <use href="#flake" x="30" y="160"/>
    <use href="#flake" x="520" y="300"/>
    <use href="#flake" x="740" y="160"/>
    <use href="#flake" x="300" y="250"/>
    <g fill="var(--snow)">
      <circle cx="250" cy="30" r="2"/><circle cx="470" cy="90" r="1.6"/><circle cx="640" cy="110" r="2"/>
      <circle cx="560" cy="30" r="1.5"/><circle cx="130" cy="150" r="1.8"/><circle cx="395" cy="230" r="1.6"/>
      <circle cx="700" cy="70" r="1.4"/><circle cx="460" cy="380" r="2"/><circle cx="560" cy="360" r="1.5"/>
      <circle cx="20" cy="30" r="1.6"/><circle cx="660" cy="400" r="1.8"/><circle cx="350" cy="330" r="1.4"/>
    </g>
  </svg>

  <header class="headline">
    <h1 class="headline-title">Glimmerbrook Jubilee LV</h1>
    <p class="headline-tagline">A Magical Holiday Festival</p>
  </header>

  <ul class="attractions">
    <li><svg width="20" height="18" viewBox="0 0 20 18"><path d="M2 10 L7 15 L18 2" fill="none" stroke="#fff" stroke-width="3.5" stroke-linecap="round" stroke-linejoin="round"/></svg>Ice skating rink</li>
    <li><svg width="20" height="18" viewBox="0 0 20 18"><path d="M2 10 L7 15 L18 2" fill="none" stroke="#fff" stroke-width="3.5" stroke-linecap="round" stroke-linejoin="round"/></svg>Snow park</li>
    <li><svg width="20" height="18" viewBox="0 0 20 18"><path d="M2 10 L7 15 L18 2" fill="none" stroke="#fff" stroke-width="3.5" stroke-linecap="round" stroke-linejoin="round"/></svg>Santa meet and greet</li>
    <li><svg width="20" height="18" viewBox="0 0 20 18"><path d="M2 10 L7 15 L18 2" fill="none" stroke="#fff" stroke-width="3.5" stroke-linecap="round" stroke-linejoin="round"/></svg>Carnival rides</li>
    <li><svg width="20" height="18" viewBox="0 0 20 18"><path d="M2 10 L7 15 L18 2" fill="none" stroke="#fff" stroke-width="3.5" stroke-linecap="round" stroke-linejoin="round"/></svg>Top food trucks</li>
    <li><svg width="20" height="18" viewBox="0 0 20 18"><path d="M2 10 L7 15 L18 2" fill="none" stroke="#fff" stroke-width="3.5" stroke-linecap="round" stroke-linejoin="round"/></svg>Millions of christmas lights</li>
    <li><svg width="20" height="18" viewBox="0 0 20 18"><path d="M2 10 L7 15 L18 2" fill="none" stroke="#fff" stroke-width="3.5" stroke-linecap="round" stroke-linejoin="round"/></svg>Giant inflatables.</li>
  </ul>

  <p class="dates">Dec 14- Dec 30</p>

  <div class="pricing">
    <p>Free for children under 48"</p>
    <p>Ticket price: presale $6, at the gate $7.</p>
    <p>Glimmer pass: $25</p>
  </div>

  <div class="partners">
    <span class="partner"><span class="partner-dot"></span>PLEM</span>
    <span class="partner">RQO</span>
  </div>

  <p class="website">glimmerbrookjubileelv.example</p>

  <div class="snapshot snapshot-santa-house" role="img" aria-label="Photo of a red-roofed Santa house decorated with garlands"></div>
  <div class="snapshot snapshot-santa-visit" role="img" aria-label="Photo of a child visiting Santa beside a Christmas tree"></div>
  <div class="snapshot snapshot-skating" role="img" aria-label="Photo of people ice skating on an outdoor rink at dusk"></div>
  <div class="snapshot snapshot-light-tree" role="img" aria-label="Photo of a glowing Christmas light tree and light displays at night"></div>
</main>
</body>
</html>
```